I am wanting to develop a new range of products called “BRISK LINE”. It will be 500mL trigger bottles of ready to use cleaning products. A Window&Glass Cleaner, Surface Sanitiser, Room Deodourant, Stainless Steel Rub, Spray&Wipe and a Sanitising Spray & Wipe. The label dimensions and shape are attached. Pellham is the shape I want but I do not like the design so don't base your design on it. SCOURBLAZE is a design I like I also like the design on the coffee packaging.

Target Market(s)

Retail and commercial kitchen

Industry/Entity Type

Cleaning Product

```html
<!DOCTYPE html>
<html lang="en">
<head>
<meta charset="utf-8">
<title>BRISK LINE – Trigger Bottle Labels</title>
<link rel="stylesheet" href="https://fonts.googleapis.com/css2?family=Montserrat:wght@300;400;700;900&display=swap">
<style>
  :root {
    --canvas: #e3e3e3;
    --navy: #1c2840;
    --brand-yellow: #f5e31a;
    --white: #ffffff;
    --glass-blue: #2f6fc4;
    --glass-photo-a: #d8dee4;
    --glass-photo-b: #8f9ba6;
    --surface-green: #4a9a2e;
    --surface-photo-a: #9a6a40;
    --surface-photo-b: #5c3a1e;
    --room-purple: #a8418f;
    --room-photo-a: #e2dbcf;
    --room-photo-b: #867b6f;
  }
  * { box-sizing: border-box; margin: 0; padding: 0; }
  html, body { width: 1200px; height: 960px; overflow: hidden; }
  body {
    background: var(--canvas);
    font-family: "Montserrat", sans-serif;
    color: var(--white);
  }
  .label-row {
    position: absolute;
    top: 270px;
    left: 0;
    width: 1200px;
    display: flex;
    justify-content: center;
    gap: 80px;
  }
  .label {
    position: relative;
    width: 320px;
    height: 420px;
    clip-path: path("M20,46 Q160,0 300,26 Q318,29 318,50 L312,392 Q310,416 286,417 L34,419 Q10,419 8,396 L2,68 Q2,50 20,46 Z");
    background: var(--band);
  }
  .label--glass   { --band: var(--glass-blue);    --photo-a: var(--glass-photo-a);   --photo-b: var(--glass-photo-b); }
  .label--surface { --band: var(--surface-green); --photo-a: var(--surface-photo-a); --photo-b: var(--surface-photo-b); }
  .label--room    { --band: var(--room-purple);   --photo-a: var(--room-photo-a);    --photo-b: var(--room-photo-b); }

  .label__photo {
    position: absolute;
    left: 0; top: 0;
    width: 320px; height: 218px;
    background: linear-gradient(160deg, var(--photo-a), var(--photo-b));
  }
  .label__splash {
    position: absolute;
    left: 0; bottom: 0;
    width: 320px; height: 92px;
    background: radial-gradient(ellipse 60% 70% at 50% 100%, rgba(255,255,255,0.55), rgba(255,255,255,0) 75%);
  }
  .maker {
    position: absolute;
    top: 38px; right: 26px;
    display: flex;
    align-items: center;
    gap: 5px;
    font-weight: 700;
    font-size: 13px;
    color: var(--white);
  }
  .maker__dot {
    width: 10px; height: 10px;
    border-radius: 50%;
    background: var(--white);
  }
  .brand {
    position: absolute;
    left: 28px; top: 76px;
    font-weight: 900;
    font-size: 60px;
    line-height: 0.95;
    letter-spacing: -1px;
    color: var(--brand-yellow);
  }
  .brand__line { display: block; }
  .brand__line--second { padding-left: 58px; }

  .product-name {
    position: absolute;
    right: 28px; top: 258px;
    font-size: 15px;
    font-weight: 300;
    letter-spacing: 0.3px;
    white-space: nowrap;
  }
  .product-name strong { font-weight: 700; }

  .claims {
    position: absolute;
    right: 30px; top: 292px;
    list-style: none;
    text-align: right;
    font-size: 10px;
    line-height: 1.35;
    font-weight: 400;
  }
  .claims strong { font-weight: 700; }

  .volume {
    position: absolute;
    left: 0; width: 320px;
    top: 378px;
    text-align: center;
    font-size: 12px;
    font-weight: 700;
    color: var(--white);
  }
</style>
</head>
<body>
<main class="label-row">

  <article class="label label--glass">
    <div class="label__photo" role="img" aria-label="Close-up photo of water droplets on glass"></div>
    <div class="label__splash" role="img" aria-label="Water splash photo"></div>
    <div class="maker"><span class="maker__dot"></span>Halvern</div>
    <h1 class="brand"><span class="brand__line">BRISK</span><span class="brand__line brand__line--second">LINE</span></h1>
    <p class="product-name"><strong>WINDOWS &amp; GLASS</strong> CLEANER</p>
    <ul class="claims">
      <li><strong>CLEANSES</strong> MOST SURFACES</li>
      <li><strong>100%</strong> ECO-FRIENDLY</li>
      <li><strong>ANTI</strong>-BACTERIAL</li>
    </ul>
    <p class="volume">500ML</p>
  </article>

  <article class="label label--surface">
    <div class="label__photo" role="img" aria-label="Photo of a wooden surface"></div>
    <div class="label__splash" role="img" aria-label="Water splash photo"></div>
    <div class="maker"><span class="maker__dot"></span>Halvern</div>
    <h1 class="brand"><span class="brand__line">BRISK</span><span class="brand__line brand__line--second">LINE</span></h1>
    <p class="product-name"><strong>SURFACE</strong> SANITISER</p>
    <ul class="claims">
      <li><strong>CLEANSES</strong> MOST SURFACES</li>
      <li><strong>100%</strong> ECO-FRIENDLY</li>
      <li><strong>ANTI</strong>-BACTERIAL</li>
    </ul>
    <p class="volume">500ML</p>
  </article>

  <article class="label label--room">
    <div class="label__photo" role="img" aria-label="Photo of a bright modern living room interior"></div>
    <div class="label__splash" role="img" aria-label="Water splash photo"></div>
    <div class="maker"><span class="maker__dot"></span>Halvern</div>
    <h1 class="brand"><span class="brand__line">BRISK</span><span class="brand__line brand__line--second">LINE</span></h1>
    <p class="product-name"><strong>ROOM</strong> DEODORANT</p>
    <ul class="claims">
      <li><strong>CLEANSES</strong> MOST SURFACES</li>
      <li><strong>100%</strong> ECO-FRIENDLY</li>
      <li><strong>ANTI</strong>-BACTERIAL</li>
    </ul>
    <p class="volume">500ML</p>
  </article>

</main>
</body>
</html>
```